Veltrix4 Business Card - Health

Veltrix4 maximizes value from the health data of its clients, including doctors, HMOs, and patients. I have attached the Veltrix4 logo as an ai and eps file.
Target Market(s)
Health, HMO, Healthcare, Data, Big Data, Data Analytics
Industry/Entity Type
Business
Requirements
Must have
- At least one side should have some white on it so that we can write on it.

```html
<!DOCTYPE html>
<html lang="en">
<head>
<meta charset="utf-8">
<title>Veltrix4 Business Card</title>
<link rel="stylesheet" href="https://fonts.googleapis.com/css2?family=Didact+Gothic&family=Open+Sans:wght@400;600&display=swap">
<style>
  :root {
    --page: #e9ecef;
    --blue-deep: #0a62b8;
    --blue-mid: #0d86d6;
    --blue-light: #22a9e4;
    --white: #ffffff;
    --paper: #f3f4f5;
    --ink: #5a5d61;
    --ink-soft: #7a7d82;
  }
  html, body {
    margin: 0;
    width: 1200px;
    height: 1062px;
    overflow: hidden;
    background: var(--page);
  }
  .canvas {
    position: relative;
    width: 1200px;
    height: 1062px;
  }
  .card {
    position: absolute;
    left: 180px;
    width: 840px;
    height: 480px;
    box-shadow: 0 10px 28px rgba(0,0,0,0.18);
  }
  .card--front { top: 34px; }
  .card--back { top: 548px; }
  .card svg { display: block; }
  .wordmark {
    font-family: "Didact Gothic", "Century Gothic", sans-serif;
  }
  .contact {
    font-family: "Open Sans", Arial, sans-serif;
  }
</style>
</head>
<body>
<main class="canvas">

  <section class="card card--front" aria-label="Business card front">
    <svg width="840" height="480" viewBox="0 0 840 480">
      <defs>
        <linearGradient id="paperFade" x1="0" y1="0" x2="1" y2="1">
          <stop offset="0" stop-color="var(--white)"/>
          <stop offset="1" stop-color="var(--paper)"/>
        </linearGradient>
        <linearGradient id="blueBand" x1="0" y1="0" x2="1" y2="0">
          <stop offset="0" stop-color="var(--blue-deep)"/>
          <stop offset="1" stop-color="var(--blue-light)"/>
        </linearGradient>
      </defs>
      <rect class="card-paper" width="840" height="480" fill="url(#paperFade)"/>
      <rect class="side-band" x="0" y="0" width="240" height="480" fill="url(#blueBand)" role="img" aria-label="Blue decorative wave area"/>

      <g class="contact">
        <text x="540" y="120" font-size="25" font-weight="600" fill="var(--blue-mid)">Marin Okafor</text>
        <text x="540" y="148" font-size="19" fill="var(--ink-soft)">CEO and Manager</text>

        <rect x="540" y="176" width="24" height="24" rx="4" fill="var(--blue-mid)"/>
        <path d="M546 182 q2 -1 3 1 l1 3 q0 1 -1 2 q2 4 5 5 q1 -1 2 -1 l3 1 q2 1 1 3 q-2 3 -5 2 q-8 -3 -11 -11 q-1 -3 2 -5 z" fill="var(--white)"/>
        <text x="574" y="195" font-size="19" fill="var(--ink-soft)">555 014 2687</text>

        <rect x="540" y="212" width="24" height="24" rx="4" fill="var(--blue-mid)"/>
        <circle cx="552" cy="224" r="7" fill="none" stroke="var(--white)" stroke-width="1.6"/>
        <path d="M545 224 H559 M552 217 V231" stroke="var(--white)" stroke-width="1.2"/>
        <text x="574" y="231" font-size="19" fill="var(--ink-soft)">www.marinokafor.com</text>

        <rect x="540" y="248" width="24" height="24" rx="4" fill="var(--blue-mid)"/>
        <text x="552" y="266" font-size="16" font-weight="600" fill="var(--white)" text-anchor="middle">@</text>
        <text x="574" y="267" font-size="19" fill="var(--ink-soft)">marin@veltrixmail.com</text>
      </g>

      <circle class="brand-dot" cx="318" cy="390" r="34" fill="var(--blue-light)"/>
      <text class="wordmark" x="372" y="420" font-size="88" fill="var(--ink)">Veltrix4</text>
    </svg>
  </section>

  <section class="card card--back" aria-label="Business card back">
    <svg width="840" height="480" viewBox="0 0 840 480">
      <defs>
        <radialGradient id="backGlow" cx="0.45" cy="0.4" r="0.8">
          <stop offset="0" stop-color="var(--blue-light)"/>
          <stop offset="0.55" stop-color="var(--blue-mid)"/>
          <stop offset="1" stop-color="var(--blue-deep)"/>
        </radialGradient>
      </defs>
      <rect class="back-field" width="840" height="480" fill="url(#backGlow)"/>
      <text class="wordmark" x="420" y="280" font-size="110" fill="var(--white)" text-anchor="middle">Veltrix4</text>
    </svg>
  </section>

</main>
</body>
</html>
```